Adelaide based cleaning and remediation business needs a website design

We are launching a new company with no clients as yet so we don't have the benefit of Trelvox Ratings to build confidence. We can use our  past work history with other employers in the industry to give some credibility. Happy to use any colour scheme as long as it look interesting when people click on the site it gets there attention. enquiry . I have supplied a mock up the important information and various photos as they tell a lot of the story.

```html
<!DOCTYPE html>
<html lang="en">
<head>
<meta charset="utf-8">
<title>Corvane Services Pty Ltd</title>
<link rel="stylesheet" href="https://fonts.googleapis.com/css2?family=Lexend:wght@500;600;700&family=Montserrat:ital,wght@0,400;0,500;0,600;1,400&display=swap">
<style>
:root{
  --orange:#f9a602;
  --orange-2:#fdbb12;
  --purple:#6163c3;
  --ink:#111;
  --text:#666;
  --beige:#f4e4c8;
  --grey:#f3f2f2;
  --card:#f4f2ef;
  --white:#fff;
}
*{box-sizing:border-box;margin:0;padding:0}
html,body{width:1200px;height:3678px;overflow:hidden}
body{position:relative;background:var(--white);font-family:"Montserrat",sans-serif;color:var(--text)}
.abs{position:absolute}
.display{font-family:"Lexend",sans-serif;font-weight:700;color:var(--ink);letter-spacing:-0.5px}
.accent-o{color:var(--orange)}
.accent-p{color:var(--purple)}
.btn{position:absolute;display:flex;align-items:center;justify-content:center;border-radius:30px;color:#fff;font-weight:600;font-size:15px}
.btn.orange{background:linear-gradient(90deg,var(--orange),var(--orange-2))}
.btn.purple{background:var(--purple)}
.photo{position:absolute;border-radius:18px;overflow:hidden}

/* hero */
.hero-band{left:0;top:0;width:1200px;height:636px;background:linear-gradient(180deg,#f3dfbd 0%,#fbf3e8 100%)}
.brand{left:89px;top:36px;font-family:"Montserrat",sans-serif;font-weight:600;font-size:22px;color:var(--ink);display:flex;align-items:center;gap:10px}
.brand i{width:14px;height:14px;background:var(--ink);display:block}
.nav{left:632px;top:42px;display:flex;gap:30px;font-size:15px;color:#333}
.nav .active{border-bottom:1.5px solid #333}
.hero-bar{left:66px;top:233px;width:4px;height:171px;background:var(--orange)}
.hero-title{left:89px;top:216px;width:520px;font-size:48px;line-height:67px;letter-spacing:-1.5px;white-space:nowrap;z-index:2}
.scroll-pill{left:89px;top:540px;width:44px;height:71px;border:1.5px solid #222;border-radius:22px}
.hero-frame{left:623px;top:113px;width:488px;height:572px;border:2px solid var(--purple);border-right:none;border-bottom:none;border-radius:30px 0 0 30px}
.hero-photo{left:633px;top:123px;width:478px;height:581px;border-radius:30px;background:linear-gradient(160deg,#4a4038,#2c6fc0 55%,#7fd23a 75%,#3b3029)}

/* services */
.section-title{font-size:44px;text-align:center;width:1200px;left:0}
.svc-card{position:absolute;top:870px;width:300px;height:399px;background:var(--card);border-radius:18px;overflow:hidden}
.svc-card .img{height:229px}
.svc-card h3{font-family:"Lexend",sans-serif;font-weight:700;color:var(--ink);font-size:16px;margin:16px 18px 6px;text-transform:uppercase;letter-spacing:-0.6px;white-space:nowrap}
.svc-card p{font-size:12.5px;line-height:18px;margin:0 18px;height:74px}
.svc-card a{display:block;margin:14px 18px;color:var(--purple);font-size:13px;text-decoration:underline}

/* about */
.about-photo{left:124px;top:1379px;width:463px;height:478px;background:linear-gradient(170deg,#b08a7a,#4b3c33 45%,#6b6560)}
.about-card{left:540px;top:1406px;width:536px;height:420px;background:#fff;border-radius:22px;box-shadow:0 20px 60px rgba(0,0,0,.07);padding:50px 41px}
.about-card h2{font-size:44px;line-height:1}
.about-card .rule{width:195px;height:3px;background:var(--orange);margin:12px 0 32px}
.about-card p{font-size:14px;line-height:20px;margin-bottom:16px}

/* pricing / qualifications */
.grey-band{left:0;top:1967px;width:1200px;height:480px;background:var(--grey)}
.feat-img{top:2017px;width:467px;height:297px}
.feat-card{top:2211px;width:388px;height:189px;background:#fff;border-radius:18px;padding:24px 22px}
.feat-card h3{font-family:"Lexend",sans-serif;font-weight:700;color:var(--ink);font-size:18px;margin-bottom:8px;letter-spacing:-0.3px}
.feat-card p{font-size:12.5px;line-height:18px}

/* testimonial */
.testi-text{left:225px;top:2705px;width:750px;text-align:center;font-style:italic;font-size:16px;line-height:25px}
.testi-name{left:0;top:2815px;width:1200px;text-align:center;font-family:"Lexend",sans-serif;font-weight:700;color:var(--ink);font-size:17px}
.dots{left:577px;top:2860px;display:flex;gap:4px}
.dots i{width:13px;height:13px;border-radius:50%;background:#ccc;display:block}
.dots i.on{background:var(--orange)}

/* quote */
.grey-bottom{left:0;top:3096px;width:1200px;height:582px;background:var(--grey)}
.quote-pill{left:187px;top:2981px;width:826px;height:229px;border-radius:115px;background:linear-gradient(90deg,var(--orange),var(--orange-2));text-align:center;color:#fff}
.quote-pill h2{font-family:"Lexend",sans-serif;font-weight:700;font-size:46px;margin-top:20px;letter-spacing:-0.5px}
.quote-pill p{font-size:14px;line-height:20px}

/* footer */
.foot-brand{left:89px;top:3380px;font-weight:600;font-size:24px;color:var(--ink);display:flex;align-items:center;gap:10px}
.foot-brand i{width:14px;height:14px;background:var(--ink);display:block}
.foot-h{font-size:25px;top:3292px}
.foot-links{left:281px;top:3334px;font-size:14px;line-height:27px;color:#666}
.contact-list{left:509px;top:3334px;font-size:13px;color:#555}
.contact-list li{list-style:none;display:flex;gap:10px;margin-bottom:10px;line-height:16px}
.contact-list svg{flex:none;margin-top:1px}
.form-card{left:816px;top:3271px;width:295px;height:278px;background:#fff;border-radius:16px}
.field{position:absolute;background:var(--grey);border-radius:20px;font-size:12.5px;color:#555;padding:12px 18px}
.rule-line{left:89px;top:3617px;width:1022px;height:1px;background:#ccc}
.copyright{left:0;top:3641px;width:1200px;text-align:center;font-size:14px;color:#777}
.to-top{left:1130px;top:3594px;width:46px;height:46px;border-radius:50%;background:var(--purple)}
</style>
</head>
<body>

<!-- hero -->
<div class="abs hero-band"></div>
<div class="abs brand"><i></i>Corvane</div>
<nav class="abs nav">
  <span class="active">Home</span><span>About Us</span><span>Services</span><span>Pricing</span>
</nav>
<div class="btn orange" style="left:963px;top:30px;width:148px;height:47px">Contact Us</div>

<div class="abs hero-bar"></div>
<div class="abs hero-frame"></div>
<div class="abs hero-photo" role="img" aria-label="Worker in blue protective suit and respirator clearing fire debris into a green tub"></div>
<h1 class="abs display hero-title">WELCOME TO<br><span class="accent-p">CORVANE</span> SERVICES<br>PTY LTD</h1>
<div class="btn orange" style="left:89px;top:439px;width:194px;height:48px">Dirty Job Cleaners</div>
<div class="btn purple" style="left:290px;top:439px;width:146px;height:48px">Get a Quote</div>
<div class="abs scroll-pill">
  <svg width="44" height="71" viewBox="0 0 44 71"><path d="M21 26v20M15 40l6 6 6-6" fill="none" stroke="#222" stroke-width="1.6"/></svg>
</div>

<!-- services -->
<h2 class="abs display section-title" style="top:796px">OUR SIGNATURE <span class="accent-o">SERVICES</span></h2>
<article class="svc-card" style="left:131px">
  <div class="img" role="img" aria-label="Pigeons perched above a droppings-stained wall" style="background:linear-gradient(180deg,#d9dde0,#b9b2a4)"></div>
  <h3>Pigeon Waste</h3>
  <p>Can cause damage to buildings &amp; spread disease, mites and bacteria, triggering alarms and damaging the reputation of businesses.</p>
  <a>Read More</a>
</article>
<article class="svc-card" style="left:450px">
  <div class="img" role="img" aria-label="Worker in white suit cleaning a fire damaged roof" style="background:linear-gradient(180deg,#8aa9c2,#6d6355 55%,#2d2a26)"></div>
  <h3>Fire Damage Clean Outs</h3>
  <p>Removal of debris On site cleaning of contents Cleaning carpets &amp; upholstered items Catalogue all contents for packing and storage</p>
  <a>Read More</a>
</article>
<article class="svc-card" style="left:767px">
  <div class="img" role="img" aria-label="Worker in protective suit clearing a cluttered room" style="background:linear-gradient(180deg,#6a6a62,#9d9a92 50%,#3e3c38)"></div>
  <h3>Squalor Estate Clean Ups</h3>
  <p>Corvane Services is a hoarding clean up firm that approaches clutter removal per sonally We always operate with comp assion...</p>
  <a>Read More</a>
</article>

<!-- about -->
<div class="photo about-photo" role="img" aria-label="Fire damaged kitchen with burnt fridge and stove"></div>
<section class="abs about-card">
  <h2 class="display">ABOUT <span class="accent-p">US</span></h2>
  <div class="rule"></div>
  <p>Adelaide-based Corvane Services is a family-run organisation. We have been in operation for more than two decades. We've gained some knowledge about cleaning and squalor removal services throughout the years.</p>
  <p>As a small South Australian company, we base everything on resp onsibility honesty and fairness .We are aware of the confidence you put in us when you seek our help.</p>
  <div class="btn orange" style="left:41px;top:316px;width:148px;height:47px">Read More</div>
</section>

<!-- pricing & qualifications -->
<div class="abs grey-band"></div>
<div class="photo feat-img" style="left:123px;background:linear-gradient(170deg,#5a4a34,#a08c5e 50%,#3d3529)" role="img" aria-label="Hoarded shed packed with tools and clutter"></div>
<div class="photo feat-img" style="left:609px;background:linear-gradient(170deg,#7b7f86,#4a4a48 50%,#b39a38 80%)" role="img" aria-label="Cleaning equipment beside a cluttered workshop floor"></div>
<div class="abs feat-card" style="left:163px">
  <h3>PRICING</h3>
  <p>Prices provided in terms of the number of hours &amp; service required or as a fixed quotation according to the quantity of clutter, pigeon faeces, and mould dis-posal expenses; however, hoarding cleaning can be different as this may require sorting and can require more organisation.</p>
</div>
<div class="abs feat-card" style="left:649px">
  <h3>QUALIFICATIONS</h3>
  <p>Mould Remediation IICRC Standard S520<br>IICRC Standard Trauma &amp; Crime Scene Cleans<br>White Card<br>Working at Heights<br>National Police Cleared<br>Working with vunerable people (DHS).</p>
</div>

<!-- testimonial -->
<h2 class="abs display section-title" style="top:2544px;line-height:50px">ONLY THE BEST SERVICE FOR<br>OUR <span class="accent-o">CUSTOMERS</span></h2>
<svg class="abs" style="left:571px;top:2654px" width="58" height="36" viewBox="0 0 58 36" aria-hidden="true">
  <g fill="#6163c3"><circle cx="14" cy="22" r="13"/><path d="M2 20 C2 8 10 1 20 0 L21 5 C14 7 10 12 10 20Z"/><circle cx="44" cy="22" r="13"/><path d="M32 20 C32 8 40 1 50 0 L51 5 C44 7 40 12 40 20Z"/></g>
</svg>
<p class="abs testi-text">Daniel and his team arrived the next morning to clean up a rental propertymy husband<br>and I own which and had been trashed &nbsp;by the tenants.<br>He was the only contractor to return my call. They did an amazing job and also deodorised<br>the house for no extra charge.</p>
<div class="abs testi-name" style="top:2817px">MARA ELLWORTH, SATISFIED CUSTOMER</div>
<div class="abs dots"><i></i><i class="on"></i><i></i></div>

<!-- quick quote -->
<div class="abs grey-bottom"></div>
<section class="abs quote-pill">
  <h2>GET A QUICK QUOTE</h2>
  <p style="margin-top:4px">Send a text to Corvane Services<br>Please enter your mobile number or email and message<br>0400555018</p>
  <div class="btn purple" style="left:340px;top:156px;width:147px;height:46px">Contact Us</div>
</section>

<!-- footer -->
<div class="abs foot-brand"><i></i>Corvane</div>
<h3 class="abs display foot-h" style="left:280px">INFORMATION</h3>
<div class="abs foot-links">Home<br>About Us<br>Services<br>Pricing<br>Contact Us</div>
<h3 class="abs display foot-h" style="left:509px">CONTACT US</h3>
<ul class="abs contact-list">
  <li><svg width="13" height="13" viewBox="0 0 24 24"><path fill="#6163c3" d="M6.6 10.8a15 15 0 0 0 6.6 6.6l2.2-2.2c.3-.3.7-.4 1-.2 1.1.4 2.3.6 3.6.6.6 0 1 .4 1 1V20c0 .6-.4 1-1 1A17 17 0 0 1 3 4c0-.6.4-1 1-1h3.5c.6 0 1 .4 1 1 0 1.3.2 2.5.6 3.6.1.3 0 .7-.2 1z"/></svg>0400 555 018</li>
  <li><svg width="13" height="13" viewBox="0 0 24 24"><path fill="#6163c3" d="M3 5h18v14H3z"/><path d="M3 5l9 7 9-7" fill="none" stroke="#fff" stroke-width="2"/></svg><span style="text-decoration:underline;color:var(--purple)">admin@corvaneservices.com</span></li>
  <li><svg width="13" height="15" viewBox="0 0 24 28"><path fill="#6163c3" d="M12 0a9 9 0 0 0-9 9c0 7 9 19 9 19s9-12 9-19a9 9 0 0 0-9-9zm0 12.5A3.5 3.5 0 1 1 12 5.5a3.5 3.5 0 0 1 0 7z"/></svg><span>Got more questions about our<br>clean-up services and what we offer?<br>Get in touch today M 0400 555 018</span></li>
</ul>
<form class="abs form-card">
  <div class="field" style="left:14px;top:20px;width:132px">Name*</div>
  <div class="field" style="left:153px;top:20px;width:132px">Email*</div>
  <div class="field" style="left:14px;top:68px;width:132px">Phone*</div>
  <div class="field" style="left:153px;top:68px;width:132px">Address*</div>
  <div class="field" style="left:14px;top:116px;width:271px;height:94px">Send A Message*</div>
  <div class="btn orange" style="left:14px;top:218px;width:147px;height:40px;font-size:14px">Submit Now</div>
</form>
<div class="abs rule-line"></div>
<div class="abs copyright">© Copyright 2025 - All Rights Reserved</div>
<div class="abs to-top"><svg width="46" height="46" viewBox="0 0 46 46"><path d="M19 25l4-4 4 4" fill="none" stroke="#fff" stroke-width="1.8"/></svg></div>

</body>
</html>
```